My project benefits Military, First Responders, Police, Fire, and Educators.

Contact Information for Business Card

2 Sided appointment card. Visual side will have my head shot with "Kestrel Works" in a bold graffic/text. I am picturing maybe the headshot applied to a filter that has a matrix effect where the picture is made up of data/numbers flowing vertically through the photo. I am of course open to other concepts as well. Side two will have contact info presented in an attractive visual complimenting the front.

```html
<!DOCTYPE html>
<html lang="en">
<head>
<meta charset="utf-8">
<title>Appointment Card</title>
<link href="https://fonts.googleapis.com/css2?family=Michroma&family=Arimo:wght@400;500&display=swap" rel="stylesheet">
<style>
  :root {
    --bg: #2a2a2a;
    --card: #050505;
    --card-edge: #111111;
    --ink: #f2f2f2;
    --ink-soft: #cfcfcf;
    --accent: #5fbf8f;
    --matrix-deep: #021208;
    --matrix-mid: #0f4a2a;
    --matrix-bright: #3fae73;
  }
  * { box-sizing: border-box; margin: 0; padding: 0; }
  html, body { width: 1200px; height: 900px; overflow: hidden; background: var(--bg); }
  .sheet {
    width: 1200px; height: 900px;
    display: flex; flex-direction: column; align-items: center; justify-content: center; gap: 40px;
  }
  .card {
    position: relative;
    width: 700px; height: 400px;
    background: var(--card);
    border: 1px solid var(--card-edge);
    overflow: hidden;
    box-shadow: 0 12px 30px rgba(0,0,0,.45);
  }

  /* Reminder side */
  .reminder { font-family: "Arimo", Arial, sans-serif; color: var(--ink); }
  .reminder__title {
    position: absolute; left: 200px; top: 72px;
    font-size: 34px; font-weight: 500; letter-spacing: .5px;
  }
  .reminder__tagline {
    position: absolute; left: 232px; top: 118px;
    font-size: 17px; color: var(--ink-soft); letter-spacing: .6px;
  }
  .reminder__line { position: absolute; height: 1.5px; background: var(--ink-soft); }
  .reminder__line--name { left: 200px; top: 182px; width: 310px; }
  .reminder__days {
    position: absolute; left: 180px; top: 212px;
    display: flex; gap: 26px; font-size: 17px; color: var(--ink-soft);
  }
  .reminder__time {
    position: absolute; left: 70px; top: 285px;
    display: flex; align-items: flex-end; gap: 8px; font-size: 17px; color: var(--ink-soft);
  }
  .blank { display: inline-block; border-bottom: 1.5px solid var(--ink-soft); height: 18px; }
  .blank--date { width: 290px; }
  .blank--hour { width: 60px; }
  .blank--min { width: 60px; }

  /* Contact side */
  .contact__portrait {
    position: absolute; left: 0; top: 0; width: 480px; height: 400px;
    background:
      radial-gradient(ellipse 38% 46% at 52% 42%, var(--matrix-bright) 0%, var(--matrix-mid) 45%, transparent 80%),
      radial-gradient(ellipse 55% 40% at 55% 95%, var(--matrix-mid) 0%, transparent 75%),
      linear-gradient(90deg, var(--matrix-deep) 0%, #03200f 50%, var(--card) 100%);
  }
  .contact__details {
    position: absolute; left: 420px; top: 112px;
    font-family: "Michroma", "Arial Black", sans-serif;
    font-variant: small-caps; color: var(--ink);
  }
  .contact__name { font-size: 26px; letter-spacing: 1px; line-height: 1; }
  .contact__rule { height: 2px; background: var(--accent); margin: 6px 0 6px; }
  .contact__rule--name { width: 220px; }
  .contact__title { font-size: 15px; letter-spacing: .6px; }
  .contact__rule--title { width: 120px; margin-top: 5px; }
  .contact__row { display: flex; align-items: center; gap: 10px; font-size: 15px; letter-spacing: 1px; margin-top: 12px; }
  .contact__icon { width: 18px; height: 18px; flex: none; }
</style>
</head>
<body>
<main class="sheet">

  <section class="card reminder" aria-label="Appointment reminder side">
    <h1 class="reminder__title">Appointment Reminder</h1>
    <p class="reminder__tagline">We look forward to seeing you</p>
    <div class="reminder__line reminder__line--name"></div>
    <div class="reminder__days">
      <span>On:</span><span>M</span><span>T</span><span>W</span><span>Th</span><span>F</span><span>S</span>
    </div>
    <div class="reminder__time">
      <span class="blank blank--date"></span>
      <span>at</span>
      <span class="blank blank--hour"></span><span>:</span><span class="blank blank--min"></span>
      <span>AM [ ]</span><span>PM [ ]</span>
    </div>
  </section>

  <section class="card contact" aria-label="Contact side">
    <div class="contact__portrait" role="img" aria-label="Head-and-shoulders portrait in a suit, rendered in green matrix-style vertical data streams"></div>
    <div class="contact__details">
      <div class="contact__name">Your Name</div>
      <div class="contact__rule contact__rule--name"></div>
      <div class="contact__title">Job Title</div>
      <div class="contact__rule contact__rule--title"></div>
      <div class="contact__row">
        <svg class="contact__icon" viewBox="0 0 18 18" aria-hidden="true">
          <rect x="5" y="1" width="8" height="16" rx="1.5" fill="none" stroke="var(--accent)" stroke-width="1.5"/>
          <line x1="8" y1="14.5" x2="10" y2="14.5" stroke="var(--accent)" stroke-width="1.5"/>
        </svg>
        <span>000 000 0000</span>
      </div>
      <div class="contact__row">
        <svg class="contact__icon" viewBox="0 0 18 18" aria-hidden="true">
          <rect x="1" y="4" width="16" height="11" fill="var(--accent)"/>
          <polyline points="1,4 9,10.5 17,4" fill="none" stroke="var(--card)" stroke-width="1.3"/>
        </svg>
        <span>youremail@xyz.com</span>
      </div>
    </div>
  </section>

</main>
</body>
</html>
```